New Electrical Contractor looking for local work

I have just started working for myself as an Electrical Contractor, based in the eastern suburbs of Melbourne. I want to advertise in the local area so hopefully I can create a client base that is close to home, so I thought a flyer that I could drop in letterboxes could be a good start. Most of my experience has been domestic houses, so ideally this is the work I would like to get more of.

Here is a list of the work I usually do:
Extensions / Renovations
Safety Switch and Switchboard Upgrades
LED Lighting including downlights/light fittings and LED strip light
Re-wires
Maintenance

I have also added a couple of images of LED strip lights and how they can be used in homes. There are a lot more on google images if anyone thinks they could be of use.

These are my details:
Business name - Dermot Hale Electrical
Phone - 0438 276 512
ABN - 52 918 407 336
REC - 37815
Email - halewireworks@brightmail.test

I will attach my business logo and business card
Updates

Could I please ask for all designs to delete the "(contractors registration number)" text.

Only REC 37815 needs to be displayed.

Thank you kindly

Industry/Entity Type

Business

Requirements
Must have
• My contact details, ie. Name, Phone, email, ABN, REC etc

```html
<!DOCTYPE html>
<html lang="en">
<head>
<meta charset="utf-8">
<title>Dermot Hale Electrical</title>
<link rel="stylesheet" href="https://fonts.googleapis.com/css2?family=Alfa+Slab+One&family=PT+Sans&family=Libre+Baskerville:wght@700&family=Tinos&display=swap">
<style>
:root{
  --frame-red:#e0201c;
  --ink-black:#000;
  --glow-blue:#2f56c9;
  --glow-deep:#0d1a57;
  --text-white:#fff;
  --photo-border:#e8e8e8;
}
*{margin:0;padding:0;box-sizing:border-box}
html,body{width:1200px;height:906px;overflow:hidden;background:#fff}
.flyer{
  position:relative;width:1200px;height:906px;
  border:7px solid var(--frame-red);
  background:
    radial-gradient(ellipse 520px 420px at 600px 540px, var(--glow-blue) 0%, #1e3a9a 35%, var(--glow-deep) 65%, var(--ink-black) 100%);
  overflow:hidden;color:var(--text-white);
}
.brand-mark{position:absolute;left:24px;top:12px;width:92px;height:92px;border-radius:50%;background:var(--text-white)}
.business-name{
  position:absolute;left:180px;top:30px;
  font-family:"Alfa Slab One",serif;font-weight:400;font-size:64px;letter-spacing:1px;line-height:1;
}
.tagline{
  position:absolute;left:0;right:0;top:108px;text-align:center;
  font-family:"PT Sans",sans-serif;font-size:35px;padding-left:10px;
}
.photo{position:absolute;border:3px solid var(--photo-border)}
.p1{left:74px;top:172px;width:232px;height:203px;background:linear-gradient(135deg,#3a2f8a,#8a7fd0 50%,#2c2470)}
.p2{left:334px;top:172px;width:240px;height:203px;background:linear-gradient(180deg,#3b2414,#a8682c 60%,#f0c060)}
.p3{left:602px;top:172px;width:238px;height:203px;background:radial-gradient(circle at 50% 60%,#6a2d5c,#1a1520 75%)}
.p4{left:884px;top:172px;width:240px;height:203px;background:linear-gradient(135deg,#cfd4da,#e9e4dc 55%,#b8a89a)}
.p5{left:74px;top:403px;width:232px;height:220px;background:linear-gradient(180deg,#2b1a0c,#8a5626 55%,#d9a25a)}
.p6{left:334px;top:403px;width:240px;height:220px;background:radial-gradient(circle at 45% 50%,#f2f2f2,#a9b0b8 55%,#5c4a3a)}
.p7{left:602px;top:403px;width:238px;height:220px;background:linear-gradient(135deg,#c9d2dc,#9aa6b4 50%,#d8b38a)}
.p8{left:884px;top:403px;width:240px;height:220px;background:linear-gradient(180deg,#eef0f2,#b8c2cc 50%,#d9c450)}
.services{
  position:absolute;left:32px;top:664px;list-style:none;white-space:nowrap;
  font-family:"Libre Baskerville",serif;font-weight:700;font-size:25px;line-height:35px;
}
.contact{
  position:absolute;left:778px;top:668px;list-style:none;white-space:nowrap;
  font-family:"Tinos",serif;font-size:28px;line-height:50px;
}
.email{
  position:absolute;right:36px;top:822px;white-space:nowrap;
  font-family:"Tinos",serif;font-size:26px;line-height:40px;
}
</style>
</head>
<body>
<main class="flyer">
  <div class="brand-mark" aria-hidden="true"></div>
  <h1 class="business-name">Dermot Hale Electrical</h1>
  <p class="tagline">For All your Electrical&nbsp; Needs</p>

  <div class="photo p1" role="img" aria-label="Hallway lit with purple LED strip lighting beside an LED tube"></div>
  <div class="photo p2" role="img" aria-label="Kitchen with warm under-cabinet LED strip lighting"></div>
  <div class="photo p3" role="img" aria-label="Coil of colour LED strip light with controller"></div>
  <div class="photo p4" role="img" aria-label="Hands fitting a wall switch with a screwdriver"></div>
  <div class="photo p5" role="img" aria-label="Wine rack with built-in warm LED lighting"></div>
  <div class="photo p6" role="img" aria-label="LED downlight globe in front of a dining room"></div>
  <div class="photo p7" role="img" aria-label="Hands joining coloured electrical wires in a conduit box"></div>
  <div class="photo p8" role="img" aria-label="Open switchboard with circuit breakers and wiring"></div>

  <ul class="services">
    <li>Extensions / Renovations</li>
    <li>Safety Switch and Switchboard Upgrades</li>
    <li>LED&nbsp; Lighting Including Downlights</li>
    <li>light fittings and LED strip light</li>
    <li>Re-wires</li>
    <li>Maintenance</li>
  </ul>

  <ul class="contact">
    <li>Tel :&nbsp; - 0438 276 512</li>
    <li>ABN - 52 918 407 336</li>
    <li>REC - 37815</li>
  </ul>
  <p class="email">Email - halewireworks@brightmail.test</p>
</main>
</body>
</html>
```